Velmar Industrial Coatings

We are looking to improve our business cards. Our company installs industrial floor and wall coatings in industrial, chemical and food processing plants.
Our coatings which consist of epoxy, urethane, and vinyl esters provide chemical and abrasion resistant surface with non-skid properties that are easy to clean.

Target Market(s)

food manufacturing, chemical plants, breweries and wineries, warehouses, clean room floors.

Industry/Entity Type

Construction

Contact Information for Business Card

improved current logo.

Colors

Designer to choose colors to be used in the design.

Requirements
Must have
• the information from uploaded file
Nice to have
• "We'll be outstanding on your floors."

```html
<!DOCTYPE html>
<html lang="en">
<head>
<meta charset="utf-8">
<title>Velmar Inc. — Business Card</title>
<link rel="stylesheet" href="https://fonts.googleapis.com/css2?family=PT+Serif:wght@400;700&family=Delius&display=swap">
<style>
  :root {
    --stage: #333333;
    --card: #e2e0e0;
    --card-light: #eeecec;
    --ink: #111111;
    --ink-soft: #2a2a2a;
    --tile: #c4c4c4;
    --photo-garden: linear-gradient(90deg, #7a8f52, #c2557f 45%, #9a9890);
    --photo-store: linear-gradient(90deg, #6b4a3a, #b9a792 50%, #5e4330);
    --photo-wood: linear-gradient(90deg, #5b3417, #a0662e 50%, #6b3c19);
    --photo-plant: linear-gradient(90deg, #7d8190, #c9ccd6 40%, #e6e8ee 70%, #a8acb8);
  }
  * { box-sizing: border-box; margin: 0; padding: 0; }
  html, body { width: 1200px; height: 900px; overflow: hidden; }
  body {
    background: var(--stage);
    font-family: "PT Serif", Georgia, serif;
    color: var(--ink);
    position: relative;
  }
  .card {
    position: absolute;
    left: 280px;
    width: 640px;
    height: 366px;
    background: linear-gradient(100deg, var(--card-light), var(--card));
    overflow: hidden;
  }
  .card--front { top: 60px; }
  .card--back { top: 474px; }

  /* brand */
  .brand {
    position: absolute;
    font-family: "PT Serif", Georgia, serif;
    font-weight: 700; color: var(--ink); line-height: 1;
    white-space: nowrap;
  }

  /* front */
  .photo { position: absolute; }
  .photo--garden { left: 0; top: 0; width: 240px; height: 70px; background: var(--photo-garden); }
  .photo--store  { left: 240px; top: 0; width: 200px; height: 130px; background: var(--photo-store); }
  .photo--wood   { left: 440px; top: 0; width: 200px; height: 196px; background: var(--photo-wood); }
  .photo--plant  {
    left: 0; top: 150px; width: 640px; height: 180px; background: var(--photo-plant);
    clip-path: polygon(0 0, 62% 0, 62% 62%, 100% 62%, 100% 100%, 0 100%);
  }
  .card--front .brand { left: 26px; top: 86px; font-size: 32px; }
  .tagline {
    position: absolute; right: 24px; top: 206px; width: 230px;
    font-family: "Delius", "Comic Sans MS", sans-serif; font-style: italic;
    font-size: 20px; line-height: 1.15; color: var(--ink);
  }

  /* back */
  .card--back .brand { left: 50px; top: 40px; font-size: 42px; }
  .person { position: absolute; left: 70px; top: 112px; }
  .person__name { font-weight: 700; font-size: 26px; margin-bottom: 8px; }
  .contact-list { list-style: none; }
  .contact-list li {
    display: flex; align-items: center; gap: 8px;
    font-size: 17px; line-height: 1.35; color: var(--ink-soft);
  }
  .icon { width: 18px; height: 18px; flex: none; }
  .tiles {
    position: absolute; left: 30px; top: 236px; width: 230px; height: 104px;
    background: linear-gradient(180deg, var(--tile), #d6d4d4);
    opacity: .8;
  }
  .office { position: absolute; left: 330px; top: 156px; }
  .office .contact-list li { font-size: 18px; }
  .address { margin-top: 8px; display: flex; gap: 8px; align-items: flex-start; }
  .address p { font-size: 18px; line-height: 1.3; color: var(--ink-soft); }
</style>
</head>
<body>

<section class="card card--front" aria-label="Card front">
  <div class="photo photo--garden" role="img" aria-label="Photo of a flower bed beside a concrete walkway"></div>
  <div class="photo photo--store" role="img" aria-label="Photo of a showroom with a coated floor"></div>
  <div class="photo photo--wood" role="img" aria-label="Photo of a decorative brown stained concrete floor"></div>
  <div class="photo photo--plant" role="img" aria-label="Photo of a bright industrial plant floor with coated surface"></div>
  <p class="brand">Velmar Inc.</p>
  <p class="tagline">We'll be outstanding on your floors.</p>
</section>

<section class="card card--back" aria-label="Card back">
  <p class="brand">Velmar Inc.</p>

  <div class="person">
    <p class="person__name">Alan Reeve</p>
    <ul class="contact-list">
      <li>
        <svg class="icon" viewBox="0 0 20 20"><circle cx="10" cy="10" r="10" fill="#111"/><rect x="7" y="4" width="6" height="12" rx="1" fill="#fff"/></svg>
        1-800-555-0142
      </li>
      <li>
        <svg class="icon" viewBox="0 0 20 20"><circle cx="10" cy="10" r="10" fill="#111"/><rect x="5" y="6.5" width="10" height="7" fill="#fff"/><path d="M5 6.5l5 4 5-4" stroke="#111" fill="none"/></svg>
        alan@velmarfloors.com
      </li>
    </ul>
  </div>

  <div class="tiles" role="img" aria-label="Decorative grey floor tiles in perspective"></div>

  <div class="office">
    <ul class="contact-list">
      <li>
        <svg class="icon" viewBox="0 0 20 20"><circle cx="10" cy="10" r="10" fill="#111"/><path d="M6 5c1-1 2 0 2.5 1.5L7.5 8c.5 1.5 2.5 3.5 4 4l1.5-1c1.5.5 2.5 1.5 1.5 2.5-1.5 1.5-4 .5-6-1.5S4.5 6.5 6 5z" fill="#fff"/></svg>
        1-360-555-0131
      </li>
      <li>
        <svg class="icon" viewBox="0 0 20 20"><circle cx="10" cy="10" r="10" fill="#111"/><rect x="7" y="4" width="6" height="12" rx="1" fill="#fff"/></svg>
        1-360-555-0177
      </li>
      <li>
        <svg class="icon" viewBox="0 0 20 20"><circle cx="10" cy="10" r="10" fill="#111"/><rect x="6" y="4.5" width="8" height="4" fill="#fff"/><rect x="4.5" y="8.5" width="11" height="5" fill="#fff"/><rect x="6.5" y="12" width="7" height="3.5" fill="#fff"/></svg>
        1-360-555-0133
      </li>
      <li>
        <svg class="icon" viewBox="0 0 20 20"><circle cx="10" cy="10" r="10" fill="#111"/><rect x="5" y="6.5" width="10" height="7" fill="#fff"/><path d="M5 6.5l5 4 5-4" stroke="#111" fill="none"/></svg>
        info@velmarfloors.com
      </li>
      <li>
        <svg class="icon" viewBox="0 0 20 20"><circle cx="10" cy="10" r="10" fill="#111"/><circle cx="10" cy="10" r="5.5" fill="none" stroke="#fff"/><ellipse cx="10" cy="10" rx="2.5" ry="5.5" fill="none" stroke="#fff"/><path d="M4.5 10h11" stroke="#fff"/></svg>
        www.velmarfloors.com
      </li>
    </ul>
    <div class="address">
      <svg class="icon" viewBox="0 0 20 20"><circle cx="10" cy="10" r="10" fill="#111"/><path d="M10 4a4 4 0 0 1 4 4c0 3-4 8-4 8s-4-5-4-8a4 4 0 0 1 4-4z" fill="#fff"/><circle cx="10" cy="8" r="1.5" fill="#111"/></svg>
      <p>Velmar Inc.<br>PO Box 412, Fernvale WA 98599</p>
    </div>
  </div>
</section>

</body>
</html>
```